Law Offices business card

Hi there, I'll need business card for the Law Offices of Tobin Haskell. The information must convey his strategic approach and quick resolution to complex business litigation needs. Please emphasize Civil Litigation, Corporate Law, Business Governance and Real Estate Law. Tobin has over 25 years of experience in these fields.The card should be modern and edgy and the message should be clear. Please consult his current website for ideas.

Business

```html
<!DOCTYPE html>
<html lang="en">
<head>
<meta charset="utf-8">
<title>Law Offices of Tobin Haskell – Business Card</title>
<link rel="stylesheet" href="https://fonts.googleapis.com/css2?family=Carlito:wght@400;700&display=swap">
<style>
  :root {
    --page-bg: #ffffff;
    --card-fill: #e2e2e2;
    --card-fill-light: #e9e9e9;
    --card-border: #a3a3a3;
    --ink-green: #0b3a0b;
    --ink-green-soft: #2f5a2f;
  }
  html, body {
    margin: 0;
    padding: 0;
    width: 1200px;
    height: 850px;
    overflow: hidden;
    background: var(--page-bg);
  }
  .canvas {
    position: relative;
    width: 1200px;
    height: 850px;
  }
  .business-card {
    display: block;
    width: 1200px;
    height: 850px;
  }
  .card-text {
    font-family: "Carlito", "Calibri", sans-serif;
    font-weight: 700;
    fill: var(--ink-green);
  }
  .name { font-size: 73px; }
  .title { font-size: 44px; }
  .firm { font-size: 44px; }
  .address, .contact { font-size: 30px; }
  .tagline { font-size: 27px; letter-spacing: 0.5px; }
  .practice-area { font-size: 21px; font-weight: 400; fill: var(--ink-green-soft); }
  .experience { font-size: 21px; letter-spacing: 1.5px; }
  .card-border { fill: var(--card-border); }
  .title-rule { stroke: var(--ink-green); stroke-width: 3; }
  .accent-bar { fill: var(--ink-green); }
  .area-mark { fill: var(--ink-green); }
</style>
</head>
<body>
<main class="canvas">
  <svg class="business-card" viewBox="0 0 1200 850" xmlns="http://www.w3.org/2000/svg" aria-label="Business card for Tobin Haskell, Attorney">
    <defs>
      <linearGradient id="cardSurface" x1="0" y1="0" x2="1" y2="1">
        <stop offset="0" stop-color="var(--card-fill)"/>
        <stop offset="0.5" stop-color="var(--card-fill-light)"/>
        <stop offset="1" stop-color="var(--card-fill)"/>
      </linearGradient>
    </defs>

    <rect class="card-border" x="117" y="61" width="917" height="635"/>
    <rect x="124" y="68" width="903" height="621" fill="url(#cardSurface)"/>

    <g class="identity">
      <text class="card-text name" x="960" y="150" text-anchor="end">Tobin Haskell</text>
      <line class="title-rule" x1="470" y1="184" x2="778" y2="184"/>
      <text class="card-text title" x="956" y="194" text-anchor="end">Attorney</text>
    </g>

    <g class="firm-block">
      <text class="card-text firm" x="968" y="270" text-anchor="end">Law Offices of Tobin Haskell, P. A.</text>
      <text class="card-text address" x="961" y="324" text-anchor="end">318B Harbor Lane</text>
      <text class="card-text address" x="961" y="362" text-anchor="end">Palm Beach, Florida 33481</text>
    </g>

    <g class="practice-block">
      <rect class="accent-bar" x="152" y="398" width="6" height="240"/>
      <text class="card-text tagline" x="176" y="424">Strategic Counsel.</text>
      <text class="card-text tagline" x="176" y="456">Swift Resolution.</text>
      <rect class="area-mark" x="176" y="489" width="8" height="8"/>
      <text class="card-text practice-area" x="194" y="498">Civil Litigation</text>
      <rect class="area-mark" x="176" y="518" width="8" height="8"/>
      <text class="card-text practice-area" x="194" y="527">Corporate Law</text>
      <rect class="area-mark" x="176" y="547" width="8" height="8"/>
      <text class="card-text practice-area" x="194" y="556">Business Governance</text>
      <rect class="area-mark" x="176" y="576" width="8" height="8"/>
      <text class="card-text practice-area" x="194" y="585">Real Estate Law</text>
      <text class="card-text experience" x="176" y="630">25+ YEARS OF EXPERIENCE</text>
    </g>

    <g class="contact-block">
      <text class="card-text contact" x="966" y="512" text-anchor="end">561-555-0142</text>
      <text class="card-text contact" x="966" y="551" text-anchor="end">561-555-0187</text>
      <text class="card-text contact" x="966" y="590" text-anchor="end">tobin@haskelllaw.com</text>
      <text class="card-text contact" x="966" y="629" text-anchor="end">www.haskelllaw.com</text>
    </g>
  </svg>
</main>
</body>
</html>
```